We need a laundry sheet packingbox desgin

-look at our website kribbelnest.nl to be in line with our house style/collor
We are a perfume seller and would like to offer also wasshingsheets with NO SMELL, so the customers can buy this incombination with our washingperfumes.
-the wassingheets will be neutrale(NO SMELL)
-it will be for the Dutch market
The next points should be on the desgin of the package
-our brand name: KRIBBELNEST
-product name: WASSTRIPS
-(contains) Bevat: 30 wasstrips
-30 wasstrips = 60 wasbeurten
Please take some inspiration of others sellers & regarding eco friendly symbols etc.:
velondra.com & plumtak.nl
Backside information will be provided afther we found the right desgin
Please look at attachement pdf open box.
Here you can find the pdf design where you need to customize:
https://qx.vz/t-rKbWnHs4Lp

```html
<!DOCTYPE html>
<html lang="nl">
<head>
<meta charset="utf-8">
<title>Kribbelnest Wasstrips – verpakking</title>
<link rel="stylesheet" href="https://fonts.googleapis.com/css2?family=Cinzel:wght@500&family=Lilita+One&family=Roboto+Condensed:wght@400;500;700&display=swap">
<style>
  :root{
    --backdrop:#dde5e6;
    --navy:#0b1a7a;
    --royal:#1740c4;
    --sky:#3aa0e8;
    --side:#4653b6;
    --side-edge:#3a459f;
    --drop-light:#eef3fb;
    --drop-mid:#b9cbec;
    --blush:#f4c3b6;
    --gold:#e3a72c;
    --band:#151617;
    --band-edge:#2b2d2f;
    --pill-green:#5bd15a;
    --pill-teal:#17a3a0;
    --white:#ffffff;
    --icon:#e9ecef;
    --title-fill:#eef1f2;
    --title-depth:#0a1660;
  }
  *{margin:0;padding:0;box-sizing:border-box}
  html,body{width:1200px;height:1062px;overflow:hidden;background:var(--backdrop)}
  .canvas{position:relative;width:1200px;height:1062px}

  .pack-side{
    position:absolute;left:224px;top:66px;width:66px;height:930px;overflow:hidden;
    background:linear-gradient(90deg,var(--side-edge),var(--side));
  }
  .side-brand{
    position:absolute;left:50%;top:160px;transform:translateX(-50%);
    display:flex;flex-direction:column;align-items:center;gap:10px;
  }
  .side-brand-dot{width:12px;height:12px;border-radius:50%;background:var(--gold)}
  .side-brand-name{
    writing-mode:vertical-rl;
    font-family:"Cinzel",serif;font-weight:500;font-size:11px;letter-spacing:.5px;color:var(--gold);
  }
  .side-title{
    position:absolute;left:50%;bottom:90px;
    writing-mode:vertical-rl;transform:translateX(-50%) rotate(180deg);
    font-family:"Roboto Condensed",sans-serif;font-weight:700;font-style:normal;
    font-size:40px;letter-spacing:1px;color:var(--white);
  }

  .pack-front{
    position:absolute;left:290px;top:66px;width:680px;height:930px;overflow:hidden;
    background:
      radial-gradient(ellipse 55% 45% at 48% 52%, var(--sky) 0%, var(--royal) 45%, transparent 75%),
      radial-gradient(ellipse 90% 80% at 50% 50%, var(--royal) 0%, var(--navy) 80%);
  }

  .hero-art{
    position:absolute;left:70px;top:70px;width:540px;height:770px;
    border-radius:50% 50% 46% 46% / 40% 40% 60% 60%;
    background:
      radial-gradient(ellipse 45% 35% at 38% 72%, var(--blush) 0%, rgba(244,195,182,0) 100%),
      radial-gradient(ellipse 60% 55% at 58% 55%, var(--drop-light) 0%, var(--drop-mid) 60%, rgba(185,203,236,0) 100%);
  }

  .brand{
    position:absolute;left:62px;top:150px;display:flex;align-items:center;gap:10px;
    font-family:"Cinzel",serif;font-weight:500;font-size:21px;letter-spacing:1px;color:var(--gold);
  }
  .brand-dot{width:14px;height:14px;border-radius:50%;background:var(--gold)}

  .product-title{
    position:absolute;left:40px;top:262px;
    font-family:"Lilita One",sans-serif;font-weight:400;font-size:112px;line-height:1;letter-spacing:-1px;
    color:var(--title-fill);white-space:nowrap;
    transform:rotate(-7deg) skewX(-10deg);transform-origin:left center;
    text-shadow:0 3px 0 #c6ced6,0 7px 0 var(--title-depth),0 10px 0 var(--title-depth),0 16px 16px rgba(0,0,0,.45);
  }

  .info-band{
    position:absolute;left:0;bottom:0;width:680px;height:94px;
    background:linear-gradient(180deg,var(--band-edge),var(--band));
    display:flex;align-items:center;padding:0 22px 0 30px;justify-content:space-between;
  }
  .contents{display:flex;flex-direction:column;gap:8px}
  .contents-pill{
    display:inline-block;padding:4px 18px;border-radius:20px;
    background:linear-gradient(90deg,var(--pill-green),var(--pill-teal));
    font-family:"Roboto Condensed",sans-serif;font-weight:500;font-size:28px;color:var(--white);
  }
  .contents-note{font-family:"Roboto Condensed",sans-serif;font-size:19px;color:var(--white);padding-left:10px}

  .badges{display:flex;gap:14px}
  .badge{display:flex;flex-direction:column;align-items:center;gap:6px;width:62px}
  .badge svg{width:34px;height:34px}
  .badge-label{font-family:"Roboto Condensed",sans-serif;font-size:10.5px;color:var(--icon);white-space:nowrap;text-transform:uppercase}
</style>
</head>
<body>
<div class="canvas">
  <aside class="pack-side">
    <div class="side-brand"><span class="side-brand-dot"></span><span class="side-brand-name">KRIBBELNEST</span></div>
    <span class="side-title">WASSTRIPS</span>
  </aside>

  <section class="pack-front">
    <div class="hero-art" role="img" aria-label="Illustratie: grote witte waterdruppel met blauwe zeepbellen en een vrouw in een wapperende roze jurk"></div>

    <div class="brand"><span class="brand-dot"></span>KRIBBELNEST</div>

    <h1 class="product-title">WASSTRIPS</h1>

    <div class="info-band">
      <div class="contents">
        <span class="contents-pill">Bevat: 30 wasstrips</span>
        <span class="contents-note">30 wasstrips = 60 wasbeurten</span>
      </div>
      <div class="badges">
        <div class="badge">
          <svg viewBox="0 0 34 34" fill="none" stroke="var(--icon)" stroke-width="1.6">
            <ellipse cx="17" cy="17" rx="14" ry="5.5"/>
            <ellipse cx="17" cy="17" rx="14" ry="5.5" transform="rotate(60 17 17)"/>
            <ellipse cx="17" cy="17" rx="14" ry="5.5" transform="rotate(-60 17 17)"/>
            <circle cx="17" cy="17" r="2.2" fill="var(--icon)"/>
          </svg>
          <span class="badge-label">Nederlands lab</span>
        </div>
        <div class="badge">
          <svg viewBox="0 0 34 34" fill="none" stroke="var(--icon)" stroke-width="1.8">
            <circle cx="17" cy="17" r="15"/>
            <path d="M17 27V16"/>
            <path d="M17 17c0-5-4-8-9-8 0 5 4 8 9 8z" fill="var(--icon)"/>
            <path d="M17 19c0-4 3-7 8-7 0 4-3 7-8 7z" fill="var(--icon)"/>
          </svg>
          <span class="badge-label">Plantaardig</span>
        </div>
        <div class="badge">
          <svg viewBox="0 0 34 34" fill="none" stroke="var(--icon)" stroke-width="3" stroke-linecap="round">
            <path d="M9 13a10 10 0 0 1 15-4"/>
            <path d="M27 17a10 10 0 0 1-7 10"/>
            <path d="M13 28a10 10 0 0 1-6-8"/>
            <path d="M22 5l3 4-5 1" stroke-width="2.2"/>
            <path d="M23 29l-4-2 3-4" stroke-width="2.2"/>
            <path d="M4 18l3 3 3-4" stroke-width="2.2"/>
          </svg>
          <span class="badge-label">Geen afval</span>
        </div>
        <div class="badge">
          <svg viewBox="0 0 34 34" fill="none" stroke="var(--icon)" stroke-width="1.6">
            <circle cx="17" cy="17" r="15"/>
            <ellipse cx="17" cy="17" rx="6.5" ry="15"/>
            <path d="M2 17h30M5 9h24M5 25h24"/>
          </svg>
          <span class="badge-label">Onze planeet</span>
        </div>
      </div>
    </div>
  </section>
</div>
</body>
</html>
```